film festival poster

We need a poster designed for our film festival. It is called the Open Horizon Cinema Week www.openhorizoncinemaweek-example.com This is a film festival about what it means to be free. We want the image to be bold and different, and yet speak about film and the importance of being a free human being. Maybe a combination of images that make up a bigger image?

Industry/Entity Type

Festival

```html
<!DOCTYPE html>
<html lang="en">
<head>
<meta charset="utf-8">
<title>Open Horizon Cinema Week – Poster</title>
<link rel="stylesheet" href="https://fonts.googleapis.com/css2?family=Yellowtail&family=Inter:wght@400;800&display=swap">
<style>
  :root {
    --title-yellow: #f2e21c;
    --title-shade: #8a7a00;
    --ink: #111111;
    --deep-blue: #1a2a9a;
    --navy: #0c1450;
    --teal: #2bb7b0;
    --magenta: #d2185a;
    --green: #2ee84a;
    --pink: #f6a6c8;
    --violet: #9a2fd8;
    --red: #f0304a;
    --pale: #fbeff3;
  }
  html, body {
    margin: 0;
    padding: 0;
    overflow: hidden;
    background: #ffffff;
  }
  .poster {
    position: relative;
    width: 856px;
    height: 1200px;
    overflow: hidden;
    background: var(--pale);
  }
  .poster__artwork {
    position: absolute;
    inset: 0;
    background:
      radial-gradient(ellipse 220px 260px at 220px 420px, var(--navy) 0%, transparent 70%),
      radial-gradient(ellipse 360px 380px at 200px 380px, var(--deep-blue) 0%, transparent 72%),
      radial-gradient(ellipse 300px 220px at 620px 110px, var(--teal) 0%, transparent 70%),
      radial-gradient(ellipse 240px 220px at 780px 240px, var(--magenta) 0%, transparent 70%),
      radial-gradient(ellipse 180px 200px at 830px 540px, var(--green) 0%, transparent 70%),
      radial-gradient(ellipse 280px 220px at 560px 930px, var(--green) 0%, transparent 70%),
      radial-gradient(ellipse 200px 180px at 330px 1000px, var(--violet) 0%, transparent 70%),
      radial-gradient(ellipse 240px 220px at 90px 1100px, var(--red) 0%, transparent 70%),
      radial-gradient(ellipse 300px 240px at 120px 780px, var(--pink) 0%, transparent 75%),
      radial-gradient(ellipse 260px 280px at 640px 560px, #ffffff 0%, transparent 70%),
      radial-gradient(ellipse 240px 180px at 90px 80px, #c9e8ff 0%, transparent 70%),
      var(--pale);
  }
  .poster__title {
    position: absolute;
    inset: 0;
    margin: 0;
    font-family: "Yellowtail", cursive;
    font-weight: 400;
    color: var(--title-yellow);
    text-shadow: 2px 3px 0 var(--title-shade), 0 0 10px rgba(0,0,0,0.25);
  }
  .poster__title-line {
    position: absolute;
    display: block;
    white-space: nowrap;
    line-height: 1;
    transform: rotate(-32deg);
    transform-origin: left bottom;
  }
  .poster__title-line--one   { left: 70px;  top: 450px; font-size: 140px; }
  .poster__title-line--two   { left: 150px; top: 640px; font-size: 140px; }
  .poster__title-line--three { left: 90px;  top: 950px; font-size: 130px; }
  .poster__brand {
    position: absolute;
    right: 46px;
    bottom: 40px;
    text-align: right;
    font-family: "Inter", sans-serif;
    color: var(--ink);
  }
  .poster__brand-name {
    display: block;
    font-size: 34px;
    font-weight: 800;
    letter-spacing: -0.5px;
    line-height: 1.05;
  }
  .poster__brand-url {
    display: block;
    margin-top: 6px;
    font-size: 11px;
    font-weight: 400;
  }
</style>
</head>
<body>
  <main class="poster">
    <div class="poster__artwork" role="img" aria-label="Abstract collage of blurred, vivid colour fields in blue, teal, magenta, green and pink"></div>
    <h1 class="poster__title">
      <span class="poster__title-line poster__title-line--one">Open</span>
      <span class="poster__title-line poster__title-line--two">Horizon</span>
      <span class="poster__title-line poster__title-line--three">Cinema Week</span>
    </h1>
    <footer class="poster__brand">
      <span class="poster__brand-name">Open Horizon</span>
      <span class="poster__brand-url">www.openhorizoncinemaweek-example.com</span>
    </footer>
  </main>
</body>
</html>
```